Business Cards Design for the electrical wholesaler: clean bold dynamic :)

We need a business card design that would follow our latest brand guidelines. As an electrical wholesaler we want to bring a fresh look and feel into the industry. The design should be clean bold and dynamic. It should come alive with the renewed energy of our green colour. Our grey colour should keep things balanced and complement the notion of maturity and responsibility. We employ Lato as a corporate font however are not bound by this font and we’re open to interpretation here.

Target Market(s)

Electrical contractors

Industry/Entity Type

Business

Contact Information for Business Card

Logo
Name & Surname: Olena Dovbush
Job Title: Director of Marketing
Email: helen.dovbush@mailvane.example
Cell phone: XXX.XXX.XXXX
Address: 20917 - 87 Ave. Edmonton, AB, Canada. T6K 2R8
Business Phone: 780.555.0187
Website: www.qorvil.example

Font styles to use
Other font styles liked:
• Lato

Requirements
Must have
• Logo & website
Nice to have
• Brand elements - some of them you may find in the attached Brand Guidelines (e.g. three lines on the background signifying "W")

```html
<!DOCTYPE html>
<html lang="en">
<head>
<meta charset="utf-8">
<title>Qorvil Business Cards</title>
<link href="https://fonts.googleapis.com/css2?family=Lato:wght@400;700&display=swap" rel="stylesheet">
<style>
  :root {
    --brand-green: #8dc63f;
    --brand-green-deep: #6a9f3c;
    --brand-grey: #58595b;
    --paper: #ffffff;
    --canvas: #ffffff;
    --card-edge: #e2e2e2;
    --card-shadow: 3px 5px 9px rgba(0, 0, 0, 0.35);
  }
  html, body {
    margin: 0;
    padding: 0;
    width: 1200px;
    height: 1000px;
    overflow: hidden;
    background: var(--canvas);
    font-family: "Lato", Arial, sans-serif;
  }
  .stage {
    position: relative;
    width: 1200px;
    height: 1000px;
  }
  .card {
    position: absolute;
    width: 734px;
    height: 420px;
    box-sizing: border-box;
    box-shadow: var(--card-shadow);
  }

  /* Back of card */
  .card--back {
    left: 360px;
    top: 473px;
    background: var(--brand-green);
    z-index: 1;
    overflow: hidden;
  }
  .back-brand-field {
    position: absolute;
    inset: 0;
    background: linear-gradient(110deg, var(--brand-green) 10%, var(--brand-green-deep) 45%, var(--brand-green) 80%);
    opacity: 0.55;
  }
  .back-lockup {
    position: absolute;
    left: 150px;
    top: 150px;
    display: flex;
    flex-direction: column;
    align-items: flex-end;
    color: var(--paper);
  }
  .back-lockup .wordmark-row {
    display: flex;
    align-items: center;
    gap: 26px;
  }
  .back-lockup .brand-dot {
    width: 84px;
    height: 84px;
    border-radius: 50%;
    background: var(--paper);
  }
  .back-lockup .wordmark {
    font-weight: 700;
    font-size: 94px;
    line-height: 1;
    letter-spacing: 1px;
  }
  .back-lockup .tagline {
    font-weight: 700;
    font-size: 14px;
    letter-spacing: 1.6px;
    margin-top: 2px;
  }

  /* Front of card */
  .card--front {
    left: 75px;
    top: 97px;
    background: var(--paper);
    border: 1px solid var(--card-edge);
    z-index: 2;
  }
  .front-lockup {
    position: absolute;
    left: 70px;
    top: 110px;
    width: 235px;
    display: flex;
    flex-direction: column;
    align-items: center;
    color: var(--brand-grey);
  }
  .front-lockup .brand-dot {
    width: 90px;
    height: 90px;
    border-radius: 50%;
    background: var(--brand-green);
    margin-bottom: 18px;
  }
  .front-lockup .wordmark {
    font-weight: 700;
    font-size: 66px;
    line-height: 1;
  }
  .front-lockup .tagline {
    font-weight: 700;
    font-size: 12.5px;
    letter-spacing: 1.4px;
    margin-top: 12px;
    white-space: nowrap;
  }
  .divider {
    position: absolute;
    left: 384px;
    top: 48px;
    width: 3px;
    height: 323px;
    background: var(--brand-green);
  }
  .contact {
    position: absolute;
    left: 415px;
    top: 42px;
    color: var(--brand-grey);
    font-size: 20px;
    line-height: 35px;
  }
  .contact p { margin: 0; }
  .contact .person-name {
    color: var(--brand-green);
    font-weight: 700;
    font-size: 28px;
    line-height: 38px;
  }
  .contact .label {
    font-weight: 700;
    display: inline-block;
    width: 22px;
  }
  .contact .label--wide { width: 30px; }
  .contact .address-block { margin-top: 18px; }
  .contact .website { font-weight: 700; }
</style>
</head>
<body>
<main class="stage">

  <section class="card card--back" aria-label="Card back">
    <div class="back-brand-field" role="img" aria-label="Green brand backdrop with broad diagonal bands"></div>
    <div class="back-lockup">
      <div class="wordmark-row">
        <span class="brand-dot"></span>
        <span class="wordmark">qorvil</span>
      </div>
      <span class="tagline">ELECTRICAL WHOLESALERS</span>
    </div>
  </section>

  <section class="card card--front" aria-label="Card front">
    <div class="front-lockup">
      <span class="brand-dot"></span>
      <span class="wordmark">qorvil</span>
      <span class="tagline">ELECTRICAL WHOLESALERS</span>
    </div>

    <div class="divider"></div>

    <div class="contact">
      <p class="person-name">Full Name</p>
      <p class="job-title">Chief Executive Officer</p>
      <p class="email">full.name@qorvil.example</p>
      <p class="phone"><span class="label label--wide">m</span>123-456-7890</p>
      <div class="address-block">
        <p>123 Main Road, Suite 345</p>
        <p>East North, State 12345</p>
        <p><span class="label">t</span>123-456-7890</p>
        <p><span class="label">f</span>123-456-7890</p>
        <p class="website">qorvil.example</p>
      </div>
    </div>
  </section>

</main>
</body>
</html>
```